Ashford Church of Grace (this will be used for new church sign) sign will be 4'x8' and would like also listed Sunday School 9:00am Worship Service 10:30am.

Logo Text

ASHFORD CHURCH OF GRACE

```html
<!DOCTYPE html>
<html lang="en">
<head>
<meta charset="utf-8">
<title>Ashford Church of Grace – Sign Variants</title>
<link href="https://fonts.googleapis.com/css2?family=Noto+Serif:wght@700&display=swap" rel="stylesheet">
<style>
  :root {
    --page: #ffffff;
    --crimson: #8b0000;
    --cream: #faeac0;
    --tan: #eccca3;
    --umber: #4a2300;
  }
  * { margin: 0; padding: 0; box-sizing: border-box; }
  html, body {
    width: 1121px;
    height: 1200px;
    overflow: hidden;
    background: var(--page);
  }
  .canvas {
    position: relative;
    width: 1121px;
    height: 1200px;
  }
  .sign {
    position: absolute;
    left: 129px;
    width: 876px;
    height: 438px;
    font-family: "Noto Serif", Georgia, serif;
    font-weight: 700;
  }
  .sign--crimson { top: 113px; background: var(--crimson); --ink: var(--cream); --pill-text: var(--crimson); }
  .sign--tan { top: 620px; background: var(--tan); --ink: var(--umber); --pill-text: var(--cream); }

  .sign__name {
    position: absolute;
    left: 0;
    right: 0;
    top: 118px;
    text-align: center;
    font-size: 142px;
    line-height: 1;
    letter-spacing: 2px;
    color: var(--ink);
  }
  .sign__tagline {
    position: absolute;
    left: 0;
    right: 0;
    top: 283px;
    height: 54px;
    display: flex;
    align-items: center;
    justify-content: center;
    gap: 14px;
  }
  .sign__subtitle {
    font-size: 40px;
    line-height: 54px;
    letter-spacing: 2px;
    color: var(--ink);
    white-space: nowrap;
  }
  .sign__rule {
    flex: 0 0 128px;
    height: 5px;
    background: var(--ink);
  }
  .sign__rule--left { clip-path: polygon(0 40%, 100% 0, 100% 100%, 0 60%); }
  .sign__rule--right { clip-path: polygon(0 0, 100% 40%, 100% 60%, 0 100%); }

  .sign__times {
    position: absolute;
    top: 368px;
    left: 95px;
    display: flex;
    gap: 14px;
  }
  .service-time {
    width: 340px;
    height: 38px;
    border-radius: 8px;
    background: var(--ink);
    color: var(--pill-text);
    font-size: 21px;
    line-height: 38px;
    text-align: center;
    letter-spacing: -0.3px;
    white-space: nowrap;
  }
</style>
</head>
<body>
  <main class="canvas">
    <section class="sign sign--crimson" aria-label="Ashford Church of Grace sign, crimson version">
      <div class="sign__name">ASHFORD</div>
      <div class="sign__tagline">
        <span class="sign__rule sign__rule--left"></span>
        <div class="sign__subtitle">CHURCH OF GRACE</div>
        <span class="sign__rule sign__rule--right"></span>
      </div>
      <div class="sign__times">
        <div class="service-time">SUNDAY SCHOOL 9:00 AM</div>
        <div class="service-time">WORSHIP SERVICE 10:30 AM</div>
      </div>
    </section>

    <section class="sign sign--tan" aria-label="Ashford Church of Grace sign, tan version">
      <div class="sign__name">ASHFORD</div>
      <div class="sign__tagline">
        <span class="sign__rule sign__rule--left"></span>
        <div class="sign__subtitle">CHURCH OF GRACE</div>
        <span class="sign__rule sign__rule--right"></span>
      </div>
      <div class="sign__times">
        <div class="service-time">SUNDAY SCHOOL 9:00 AM</div>
        <div class="service-time">WORSHIP SERVICE 10:30 AM</div>
      </div>
    </section>
  </main>
</body>
</html>
```